Terrace Anchoring Solutions business card

As per your previous logo design, I would like to incorporate all those colours into the card.
I've added a business card I don't mind which is double sided. Also my Po box number..
Could be in a format so I can add new email, ph numbers etc.

Thanks

• My logo that is attached and the same colour scheme

```html
<!DOCTYPE html>
<html lang="en">
<head>
<meta charset="utf-8">
<title>Terrace Anchoring Solutions – Business Card</title>
<link rel="stylesheet" href="https://fonts.googleapis.com/css2?family=Arimo:wght@400;700&display=swap">
<style>
  :root {
    --bg: #2a2a2a;
    --sky-light: #7fd0f7;
    --sky-deep: #2c98d6;
    --ink: #111111;
    --paper: #ffffff;
    --mark-dark: #1f1f1f;
  }
  * { margin: 0; padding: 0; box-sizing: border-box; }
  html, body {
    width: 1200px; height: 900px; overflow: hidden;
    background: var(--bg);
    font-family: "Arimo", Arial, sans-serif;
  }
  .sheet {
    width: 1200px; height: 900px;
    display: flex; flex-direction: column;
    align-items: center; justify-content: center; gap: 40px;
  }
  .card {
    width: 620px; height: 354px;
    position: relative; overflow: hidden;
    box-shadow: 0 8px 24px rgba(0,0,0,.45);
  }
  .card--front {
    background: linear-gradient(160deg, var(--sky-light), var(--sky-deep));
    display: flex; align-items: center; justify-content: center;
  }
  .card--back { display: flex; background: var(--paper); }
  .brand {
    display: flex; align-items: center; gap: 12px;
    font-weight: 700; color: var(--mark-dark);
    font-size: 26px; line-height: 1.1;
  }
  .brand__square {
    width: 28px; height: 28px; flex: none;
    background: var(--mark-dark);
  }
  .card--front .brand { color: var(--mark-dark); }
  .card__logo-side {
    width: 47%;
    display: flex; align-items: center; justify-content: center;
    padding: 0 24px;
  }
  .card__logo-side .brand { font-size: 22px; }
  .card__info {
    flex: 1;
    background: linear-gradient(160deg, var(--sky-light), var(--sky-deep));
    padding: 42px 28px 0 26px;
    color: var(--ink);
  }
  .person__name { font-size: 26px; font-weight: 700; letter-spacing: .3px; }
  .person__title { font-size: 17px; color: var(--paper); margin-top: 4px; }
  .contacts { list-style: none; margin-top: 28px; }
  .contacts li {
    display: flex; align-items: center; gap: 12px;
    font-size: 17px; margin-bottom: 10px;
  }
  .contacts svg { width: 22px; height: 22px; flex: none; }
  .company { margin-top: 22px; font-size: 16px; line-height: 1.25; }
  .company__hotline { font-weight: 700; }
  .company__name { font-weight: 700; color: var(--paper); }
</style>
</head>
<body>
<main class="sheet">
  <section class="card card--front" aria-label="Card front">
    <div class="brand"><span class="brand__square"></span>Terrace Anchoring Solutions</div>
  </section>

  <section class="card card--back" aria-label="Card back">
    <div class="card__logo-side">
      <div class="brand"><span class="brand__square"></span>Terrace Anchoring Solutions</div>
    </div>
    <div class="card__info">
      <h1 class="person__name">YOUR NAME</h1>
      <p class="person__title">Title</p>
      <ul class="contacts">
        <li>
          <svg viewBox="0 0 24 24" aria-hidden="true"><circle cx="12" cy="12" r="12" fill="#fff"/><path d="M8.2 6.5l2 2.3-1.1 1.4a8 8 0 0 0 4.7 4.7l1.4-1.1 2.3 2-1 1.9c-4.8-.3-8.9-4.4-9.2-9.2z" fill="#111"/></svg>
          0400 518 273
        </li>
        <li>
          <svg viewBox="0 0 24 24" aria-hidden="true"><circle cx="12" cy="12" r="12" fill="#fff"/><rect x="6" y="8" width="12" height="8" fill="#111"/><path d="M6 8l6 4.5L18 8" fill="none" stroke="#fff" stroke-width="1"/></svg>
          director@terraceanchoring.com.au
        </li>
      </ul>
      <p class="company">
        <span class="company__hotline">1800 SLOPEFIX</span><br>
        <span class="company__name">Terrace Anchoring Solutions.</span><br>
        P.O.Box 418 Hillcrest,<br>
        NSW 2301
      </p>
    </div>
  </section>
</main>
</body>
</html>
```